Book Cover for Notes on the Quiet River's Far Lamps

I need a book cover for a 6 x 9 paperback titled Notes on the Quiet River's Far Lamps Gathered by Sailors and Weavers Resting in the Valley beyond the Northern Valley. It has to do with consciousness, the mind, incarnation onto Earth, leaving Earth, and the life in the life after this life. I have an idea I'm providing with this description, but I am open to anything that would be striking and stimulating, whether with a book or not. I am the author, T. Warren Blakely. I've added another background idea to see if anyone can do something with it and I've increased the budget.

```html
<!DOCTYPE html>
<html lang="en">
<head>
<meta charset="utf-8">
<title>Notes on the Quiet River's Far Lamps — Cover Presentation</title>
<link href="https://fonts.googleapis.com/css2?family=Lexend+Giga:wght@500;600;700&family=Raleway:wght@500;600;700&family=Source+Serif+4:wght@400;600&display=swap" rel="stylesheet">
<style>
  :root {
    --board-light: #fbfbfb;
    --board-edge: #d6d6d6;
    --ink-dark: #111111;
    --night: #363650;
    --night-top: #45425c;
    --spine: #433a52;
    --spine-top: #493d55;
    --rose-light: #c9a3c3;
    --rose-accent: #a66f9c;
    --rose-author: #a7739b;
    --outline: #55536f;
    --quote-ink: #e4e0ea;
    --flap-paper: #f2f1f4;
    --flap-ink: #1b1b22;
    --title-font: "Lexend Giga", "Arial Black", sans-serif;
    --serif-font: "Source Serif 4", Georgia, serif;
    --sans-font: "Raleway", Arial, sans-serif;
  }

  * { box-sizing: border-box; margin: 0; padding: 0; }

  html, body {
    width: 1200px;
    height: 1200px;
    overflow: hidden;
  }

  body {
    position: relative;
    background: radial-gradient(ellipse at 50% 45%, var(--board-light) 0%, #f0f0f0 55%, var(--board-edge) 100%);
    font-family: var(--sans-font);
  }

  /* ---------- Full cover spread (back · spine · front) ---------- */
  .spread {
    position: absolute;
    width: 935px;
    height: 565px;
    overflow: hidden;
    transform-origin: 0 0;
  }
  .spread--hardcover { left: 121px; top: 42px; }
  .spread--paperback { left: 216px; top: 691px; transform: scale(0.7957); }

  .back-panel {
    position: absolute;
    left: 0; top: 0;
    width: 426px; height: 565px;
    background: linear-gradient(180deg, var(--night-top) 0%, #3b3a54 50%, var(--night) 100%);
  }

  .title-stack {
    font-family: var(--title-font);
    font-weight: 700;
    font-size: 36px;
    line-height: 36px;
    letter-spacing: -0.04em;
    text-transform: uppercase;
  }
  .title-stack .line { display: block; white-space: nowrap; height: 36px; }
  .title-stack .line--final { font-size: 52px; line-height: 50px; height: 50px; margin-top: 2px; }

  .back-panel .title-stack {
    position: absolute;
    left: 39px; top: 140px;
    color: transparent;
    -webkit-text-stroke: 0.8px var(--outline);
  }

  .endorsement {
    position: absolute;
    left: 39px; top: 432px;
    width: 262px;
    font-family: var(--serif-font);
    color: var(--quote-ink);
    font-size: 7.4px;
    line-height: 12px;
  }
  .endorsement__source {
    position: absolute;
    left: 39px; top: 498px;
    font-family: var(--serif-font);
    font-weight: 600;
    font-size: 9.5px;
    color: var(--quote-ink);
  }

  .spine {
    position: absolute;
    left: 426px; top: 0;
    width: 85px; height: 565px;
    background: linear-gradient(180deg, var(--spine-top) 0%, var(--spine) 100%);
  }
  .spine__title {
    position: absolute;
    top: 50px; left: 17px;
    height: 300px;
    writing-mode: vertical-rl;
    font-family: var(--title-font);
    font-weight: 600;
    font-size: 10px;
    line-height: 14px;
    letter-spacing: -0.02em;
    color: var(--rose-light);
    text-transform: uppercase;
    white-space: nowrap;
  }
  .spine__author {
    position: absolute;
    top: 392px; left: 36px;
    writing-mode: vertical-rl;
    font-family: var(--title-font);
    font-weight: 600;
    font-size: 11px;
    letter-spacing: 0;
    color: var(--rose-author);
    text-transform: uppercase;
    white-space: nowrap;
  }

  .front-panel {
    position: absolute;
    left: 511px; top: 0;
    width: 424px; height: 565px;
    background: var(--night);
  }
  .front-panel__glow {
    position: absolute;
    inset: 0;
    background:
      radial-gradient(ellipse 62% 58% at 48% 2%, #a06a8a 0%, #87597a 22%, #6c4b69 40%, #54405c 56%, rgba(62,56,82,0) 78%),
      linear-gradient(180deg, #403a55 0%, #383750 55%, var(--night) 100%);
  }
  .front-panel .title-stack {
    position: absolute;
    right: 60px; top: 140px;
    text-align: right;
    color: var(--rose-light);
  }
  .front-panel .title-stack .accent { color: var(--rose-accent); }
  .front-panel__author {
    position: absolute;
    right: 56px; top: 505px;
    font-family: var(--title-font);
    font-weight: 600;
    font-size: 11.5px;
    letter-spacing: 0;
    color: var(--rose-author);
    text-transform: uppercase;
    white-space: nowrap;
  }

  /* ---------- Paperback flaps ---------- */
  .flap {
    position: absolute;
    top: 691px;
    height: 449px;
    background: var(--flap-paper);
    color: var(--flap-ink);
  }
  .flap--left  { left: 43px;  width: 173px; }
  .flap--right { left: 960px; width: 175px; }

  .flap__credit {
    position: absolute;
    left: 24px; top: 130px;
    font-size: 6.2px;
    font-weight: 700;
  }
  .flap__copy {
    position: absolute;
    font-size: 5.9px;
    line-height: 8.5px;
    font-weight: 600;
  }
  .flap--left .flap__copy { left: 24px; width: 120px; }
  .flap--right .flap__copy { left: 24px; width: 118px; }

  .flap__lead {
    font-family: var(--serif-font);
    font-weight: 600;
    text-transform: uppercase;
  }

  .flap__heading {
    position: absolute;
    left: 24px; top: 28px;
    font-size: 12.5px;
    line-height: 20.5px;
    font-weight: 600;
    text-transform: uppercase;
  }

  /* ---------- Labels ---------- */
  .board-label {
    position: absolute;
    width: 300px;
    text-align: center;
    font-family: var(--sans-font);
    font-weight: 700;
    font-size: 22px;
    color: var(--ink-dark);
  }
  .board-label--hardcover { left: 441px; top: 614px; }
  .board-label--paperback { left: 441px; top: 1150px; }
</style>
</head>
<body>

  <!-- Hardcover spread -->
  <section class="spread spread--hardcover">
    <div class="back-panel">
      <h2 class="title-stack" aria-hidden="true">
        <span class="line">NotesOn</span>
        <span class="line">TheQuiet</span>
        <span class="line">River’s</span>
        <span class="line">FarLamps</span>
        <span class="line">GatheredBy</span>
        <span class="line">SailorsAnd</span>
        <span class="line line--final">Beyond</span>
      </h2>
      <p class="endorsement">“Every page reads like a lantern held over dark water, patient and unhurried. The author gathers the voices of those who crossed before us and lets them speak plainly, so that the far shore feels less like a rumor and more like a place one might someday recognise as home.”</p>
      <p class="endorsement__source">— Maren Oskeld —</p>
    </div>
    <div class="spine">
      <p class="spine__title">Notes on the Quiet<br>River’s Far Lamps<br>Gathered by Sailors<br>in the Valley Beyond</p>
      <p class="spine__author">T. Warren Blakely</p>
    </div>
    <div class="front-panel">
      <div class="front-panel__glow" role="img" aria-label="Layered rose mist rising from dark water, glowing pink at the top and fading into deep violet night"></div>
      <h1 class="title-stack">
        <span class="line">Notes<span class="accent">On</span></span>
        <span class="line"><span class="accent">The</span>Quiet</span>
        <span class="line">River’s</span>
        <span class="line"><span class="accent">Far</span>Lamps</span>
        <span class="line">Gathered<span class="accent">By</span></span>
        <span class="line">Sailors<span class="accent">And</span></span>
        <span class="line line--final">Beyond</span>
      </h1>
      <p class="front-panel__author">T. Warren Blakely</p>
    </div>
  </section>
  <p class="board-label board-label--hardcover">cover</p>

  <!-- Paperback with flaps -->
  <aside class="flap flap--left">
    <p class="flap__credit">By: The Photographer</p>
    <p class="flap__copy" style="top:151px;">The cover image was made at dusk on a long lake, where the last light lingers above the water and slowly gathers into a soft rose glow. Nothing was added afterward; the colours are simply what the evening offered while the shore grew quiet and still.</p>
    <p class="flap__copy" style="top:242px;">Each layer of tone is a band of mist lifting off the surface, stacked one above another until the darkness below feels deep and calm, like a held breath.</p>
    <p class="flap__copy" style="top:317px;">It is offered here as a small doorway, a place to pause before turning the first page and stepping out onto the river with the sailors and weavers.</p>
  </aside>

  <section class="spread spread--paperback">
    <div class="back-panel">
      <h2 class="title-stack" aria-hidden="true">
        <span class="line">NotesOn</span>
        <span class="line">TheQuiet</span>
        <span class="line">River’s</span>
        <span class="line">FarLamps</span>
        <span class="line">GatheredBy</span>
        <span class="line">SailorsAnd</span>
        <span class="line line--final">Beyond</span>
      </h2>
      <p class="endorsement">“Every page reads like a lantern held over dark water, patient and unhurried. The author gathers the voices of those who crossed before us and lets them speak plainly, so that the far shore feels less like a rumor and more like a place one might someday recognise as home.”</p>
      <p class="endorsement__source">— Maren Oskeld —</p>
    </div>
    <div class="spine">
      <p class="spine__title">Notes on the Quiet<br>River’s Far Lamps<br>Gathered by Sailors<br>in the Valley Beyond</p>
      <p class="spine__author">T. Warren Blakely</p>
    </div>
    <div class="front-panel">
      <div class="front-panel__glow" role="img" aria-label="Layered rose mist rising from dark water, glowing pink at the top and fading into deep violet night"></div>
      <h2 class="title-stack">
        <span class="line">Notes<span class="accent">On</span></span>
        <span class="line"><span class="accent">The</span>Quiet</span>
        <span class="line">River’s</span>
        <span class="line"><span class="accent">Far</span>Lamps</span>
        <span class="line">Gathered<span class="accent">By</span></span>
        <span class="line">Sailors<span class="accent">And</span></span>
        <span class="line line--final">Beyond</span>
      </h2>
      <p class="front-panel__author">T. Warren Blakely</p>
    </div>
  </section>

  <aside class="flap flap--right">
    <h3 class="flap__heading">About<br>This<br>Book</h3>
    <p class="flap__copy" style="top:111px;"><span class="flap__lead">What waits on the far shore,</span> this book gathers accounts from people who have glimpsed the valley beyond and returned to tell of it. Their words are set down simply, without ornament, so that readers may weigh them for themselves and find what rings true. Each chapter follows one voice.</p>
    <p class="flap__copy" style="top:229px;"><span class="flap__lead">Across twenty years of listening,</span> the author has kept careful notes on the mind, on arriving into this world and on leaving it again. These notes ask how awareness travels, what it carries along, and why so many who return describe the same gentle lamps burning across the water. The answers are drawn from science, from memory and from the quiet testimony of those who rest beyond the northern valley.</p>
    <p class="flap__copy" style="top:356px;"><span class="flap__lead">For anyone who has wondered,</span> these pages offer company and calm, a steady light to read by when the evening grows long and still.</p>
  </aside>
  <p class="board-label board-label--paperback">soft cover</p>

</body>
</html>
```